Book Cover Design for first time business owners

Looking for a design for my book, 'LAYING THE GROUNDWORK' subtitle is
THE REAL ESTATE, DESIGN, & CONSTRUCTION STEPS TO OPENING YOUR RETAIL OR FOOD-SERVICE CONCEPT ON-TIME AND ON BUDGET

If it helps, below is part of the preface:

These pages derive from my experiences and industry standards. This book runs through the budgeting, real estate, design, construction, signage, and equipment processes needed to get any retail or restaurant space open on-time and on budget while saving you time, money, and headaches along the way.

Whether it be a one-off enterprise or franchise, flower shop, or swim center; the steps and procedures are strikingly similar. Whether you’re looking to spend $200,000 or $2,000,000, it’s all largely the same.
This book does not discuss marketing or operations as those items are more concept specific, and outside the confines of this book.
Technically food-service concepts (restaurants, cafés, and bars) are not considered retail. For the basis of this book and to streamline writing, mentions of retail include food-service concepts.

Target Market(s)

First time business Owners looking to construct a retail or food-service concept

Font styles to use
Serif

Requirements
Must have
• I'm open to any designs! Looking for the design to wrap around the front, spine, and back.
• Please include the authors name on the front: Corwin Halbeck. The Authors name size should not be overly intrusive.
• I'm still working on the verbiage for the back of the book. That verbiage will be on the top half of the back.

```html
<!DOCTYPE html>
<html lang="en">
<head>
<meta charset="utf-8">
<title>Laying the Groundwork — Front Cover</title>
<link rel="stylesheet" href="https://fonts.googleapis.com/css2?family=Tinos&family=Rajdhani:wght@700&display=swap">
<style>
  :root {
    --paper: #f8f8f7;
    --paper-mid: #e4e4e2;
    --paper-deep: #cfcfcc;
    --title-red: #e0242b;
    --title-dark: #3a3a3c;
    --band: #48484a;
    --band-text: #ffffff;
    --author: #4a4a4a;
  }
  * { margin: 0; padding: 0; box-sizing: border-box; }
  html, body {
    width: 993px;
    height: 1200px;
    overflow: hidden;
    background: var(--paper);
  }
  .cover {
    position: relative;
    width: 993px;
    height: 1200px;
    overflow: hidden;
  }
  .cover-artwork {
    position: absolute;
    inset: 0;
    background:
      linear-gradient(115deg, rgba(0,0,0,0) 0%, rgba(0,0,0,0) 28%, rgba(255,255,255,0.9) 34%, rgba(255,255,255,0.9) 42%, rgba(0,0,0,0) 48%),
      radial-gradient(ellipse at 75% 80%, var(--paper) 0%, rgba(248,248,247,0) 55%),
      linear-gradient(160deg, var(--paper) 0%, var(--paper-mid) 45%, var(--paper-deep) 100%);
  }
  .title {
    position: absolute;
    top: 72px;
    left: 0;
    right: 0;
    font-family: "Tinos", "Times New Roman", serif;
    font-weight: 400;
    line-height: 0.9;
  }
  .title-line { display: block; white-space: nowrap; }
  .title-line--accent {
    color: var(--title-red);
    font-size: 124px;
    padding-left: 48px;
  }
  .title-line--main {
    color: var(--title-dark);
    font-size: 114px;
    padding-left: 100px;
  }
  .subtitle-band {
    position: absolute;
    top: 405px;
    left: 0;
    width: 993px;
    height: 200px;
    background: var(--band);
    display: flex;
    align-items: center;
    justify-content: center;
  }
  .subtitle {
    font-family: "Rajdhani", "Arial Narrow", sans-serif;
    font-weight: 700;
    font-size: 40px;
    line-height: 1.1;
    color: var(--band-text);
    text-align: center;
    text-transform: uppercase;
  }
  .author {
    position: absolute;
    right: 60px;
    bottom: 62px;
    font-family: "Rajdhani", "Arial Narrow", sans-serif;
    font-weight: 700;
    font-size: 48px;
    letter-spacing: 1px;
    color: var(--author);
    text-transform: uppercase;
  }
</style>
</head>
<body>
  <main class="cover">
    <div class="cover-artwork" role="img" aria-label="Close-up of architectural floor plan drawings with wall lines, a door swing and room labels on white paper, crossed by a diagonal white strip"></div>

    <h1 class="title">
      <span class="title-line title-line--accent">LAYING THE</span>
      <span class="title-line title-line--main">GROUNDWORK</span>
    </h1>

    <div class="subtitle-band">
      <p class="subtitle">
        The real estate, design, &amp; construction steps to<br>
        opening your retail or food-service concept<br>
        on-time and on budget
      </p>
    </div>

    <p class="author">Corwin Halbeck</p>
  </main>
</body>
</html>
```